(Expedite) Business Card
Pacific Motor Keep
(Expedite) Business Card - Real Estate
Creative Brief
Use standard fonts
please be creative - ok to use a different font than the logo
Professional
State-of-the-Art Car Storage & Collection Management
27405 W. Lindenmoor Avenue Santa Paula, CA 93071
info@pacificmotorkeep.com
www.pacificmotorkeep.com
Logo on front of business card, contact information on back of business card.
Contact information on back of business card.
PacificMotorKeep PacificMotorKeep

```html
<!DOCTYPE html>
<html lang="en">
<head>
<meta charset="utf-8">
<title>Pacific Motor Keep — Business Card</title>
<link href="https://fonts.googleapis.com/css2?family=Montserrat:wght@800&family=Open+Sans:wght@400;600;700&display=swap" rel="stylesheet">
<style>
  :root {
    --canvas: #8a8b8d;
    --orange: #f2661c;
    --orange-deep: #e0520f;
    --ink: #1b1b1b;
    --paper: #ffffff;
    --muted: #555555;
    --rule: #c9c9c9;
  }
  * { box-sizing: border-box; margin: 0; padding: 0; }
  html, body { width: 1200px; height: 908px; overflow: hidden; }
  body {
    background: var(--canvas);
    font-family: "Open Sans", Arial, sans-serif;
    position: relative;
  }
  .card {
    position: absolute;
    width: 640px;
    height: 366px;
    border-radius: 22px;
    overflow: hidden;
  }
  /* Front */
  .card-front {
    left: 120px; top: 68px;
    background: linear-gradient(135deg, var(--orange) 0%, var(--orange-deep) 100%);
  }
  .front-brand {
    position: absolute; left: 56px; top: 118px;
    display: flex; align-items: center; gap: 14px;
  }
  .brand-square { flex: none; width: 22px; height: 22px; background: var(--ink); }
  .front-brand .brand-name {
    font-family: "Montserrat", Arial, sans-serif;
    font-weight: 800; font-size: 34px; letter-spacing: 0.5px;
    color: var(--ink); text-transform: uppercase; line-height: 1;
    white-space: nowrap;
  }
  .front-rule {
    position: absolute; left: 56px; top: 170px;
    width: 440px; height: 2px; background: var(--ink);
  }
  .tagline {
    position: absolute; left: 56px; top: 186px;
    color: var(--paper); font-size: 15px; font-weight: 600;
  }
  /* Back */
  .card-back {
    left: 440px; top: 474px;
    background: var(--paper);
  }
  .back-brand {
    position: absolute; left: 40px; top: 100px;
    display: flex; align-items: center; gap: 12px;
  }
  .back-brand .brand-square { width: 18px; height: 18px; }
  .back-brand .brand-name {
    font-family: "Montserrat", Arial, sans-serif;
    font-weight: 800; font-size: 22px; color: var(--ink);
    text-transform: uppercase; line-height: 1.05; width: 220px;
  }
  .person { position: absolute; left: 118px; top: 196px; }
  .person-name { color: var(--orange); font-weight: 700; font-size: 19px; }
  .person-role { color: var(--ink); font-size: 13px; font-weight: 600; margin-top: 2px; }
  .divider {
    position: absolute; left: 338px; top: 52px;
    width: 1px; height: 190px; background: var(--rule);
  }
  .contact {
    position: absolute; left: 360px; top: 56px;
    list-style: none; display: flex; flex-direction: column; gap: 10px;
    font-size: 12px; color: var(--muted);
  }
  .contact li { display: flex; align-items: center; gap: 10px; line-height: 1.35; }
  .contact .icon {
    flex: none; width: 22px; height: 22px; border-radius: 50%;
    background: var(--orange); display: flex; align-items: center; justify-content: center;
  }
  .band-rule {
    position: absolute; left: 0; right: 0; bottom: 62px;
    height: 4px; background: var(--orange);
  }
  .band {
    position: absolute; left: 0; right: 0; bottom: 0; height: 56px;
    background: var(--ink); color: var(--paper);
    display: flex; align-items: center; justify-content: flex-end;
    padding-right: 48px; font-size: 15px; letter-spacing: 2px; font-weight: 600;
  }
</style>
</head>
<body>

<section class="card card-front" aria-label="Business card front">
  <div class="front-brand">
    <span class="brand-square"></span>
    <span class="brand-name">Pacific Motor Keep</span>
  </div>
  <div class="front-rule"></div>
  <p class="tagline">State-of-the-Art Car Storage &amp; Collection Management</p>
</section>

<section class="card card-back" aria-label="Business card back">
  <div class="back-brand">
    <span class="brand-square"></span>
    <span class="brand-name">Pacific Motor Keep</span>
  </div>
  <div class="person">
    <p class="person-name">Your Name</p>
    <p class="person-role">Position</p>
  </div>
  <div class="divider"></div>
  <ul class="contact">
    <li>
      <span class="icon"><svg width="12" height="12" viewBox="0 0 24 24"><path fill="#fff" d="M12 2a7 7 0 0 0-7 7c0 5 7 13 7 13s7-8 7-13a7 7 0 0 0-7-7zm0 9.5A2.5 2.5 0 1 1 12 6.5a2.5 2.5 0 0 1 0 5z"/></svg></span>
      <span>27405 W. Lindenmoor Avenue<br>Larkspur Hollow, NV 89071</span>
    </li>
    <li>
      <span class="icon"><svg width="12" height="12" viewBox="0 0 24 24"><path fill="#fff" d="M6.6 10.8a15 15 0 0 0 6.6 6.6l2.2-2.2a1 1 0 0 1 1-.25 11.4 11.4 0 0 0 3.6.57 1 1 0 0 1 1 1V20a1 1 0 0 1-1 1A17 17 0 0 1 3 4a1 1 0 0 1 1-1h3.5a1 1 0 0 1 1 1c0 1.25.2 2.45.57 3.57a1 1 0 0 1-.25 1z"/></svg></span>
      <span>(555) 010-2471</span>
    </li>
    <li>
      <span class="icon"><svg width="12" height="12" viewBox="0 0 24 24"><path fill="#fff" d="M6.6 10.8a15 15 0 0 0 6.6 6.6l2.2-2.2a1 1 0 0 1 1-.25 11.4 11.4 0 0 0 3.6.57 1 1 0 0 1 1 1V20a1 1 0 0 1-1 1A17 17 0 0 1 3 4a1 1 0 0 1 1-1h3.5a1 1 0 0 1 1 1c0 1.25.2 2.45.57 3.57a1 1 0 0 1-.25 1z"/></svg></span>
      <span>(555) 010-3896</span>
    </li>
    <li>
      <span class="icon"><svg width="12" height="12" viewBox="0 0 24 24"><path fill="#fff" d="M3 5h18v14H3z"/><path fill="none" stroke="#f2661c" stroke-width="1.8" d="M3 5l9 7 9-7"/></svg></span>
      <span>info@pacificmotorkeep.com</span>
    </li>
  </ul>
  <div class="band-rule"></div>
  <div class="band">www.pacificmotorkeep.com</div>
</section>

</body>
</html>
```